Simple templates for management consulting firm

Vireo Associates is a management consulting firm based in the DC area. We have all the basic templates but would like to tweak them so they look consistent.

Check us out at www.vireoassociates-example.com

For this project we would like to get
a tweaked powerpoint template (header should be up)
a letter template for letters
a fax template

Current templates and our logo are attached.
Updates

We just increased the budget of this project.

We got questions about the project. Here are our thoughts on this one:

Please include the logo into the fax template. If you find improvements in the layout then feel free to make those. Let's not overthink this too much. Keep it simple :)

We like The powerpoint concept as is. The slide titles are for some reasons on the bottom. It seems to irritate some folks. If you can switch the slide titles to the top, keep the look and feel of the slides and work in the logo then that would be fantastic.

The letter head should include the following

Vireo Associates, LLC Box 5827, Millbrook, VA 20147 Phone 703 518-9461, Fax 703 286 7135, www.vireoassociates-example.com and the logo.

Again, let's keep it simple.

Thank you for considering this project.

We just realize that we are not necessarily inisting to use the red in the slides.
Any approach that would work with the logo will be considered.

Thanks for your creativity.

Target Market(s)

tech companies, Pinnacle 400, venture capitalists

Industry/Entity Type

Management Consulting

Requirements
Must have
• Keep it simple please

```html
<!DOCTYPE html>
<html lang="en">
<head>
<meta charset="utf-8">
<title>Vireo Associates – Fax Cover</title>
<link rel="stylesheet" href="https://fonts.googleapis.com/css2?family=Open+Sans:wght@400;600;700&display=swap">
<style>
  :root {
    --brand-red: #7e1600;
    --ink: #111111;
    --rule: #8a8a8a;
    --logo-text: #dcdcdc;
    --logo-dot: #d9a93a;
    --paper: #ffffff;
  }
  html, body {
    margin: 0;
    padding: 0;
    overflow: hidden;
    background: var(--paper);
  }
  .sheet {
    position: relative;
    width: 927px;
    height: 1200px;
    overflow: hidden;
    background: var(--paper);
    font-family: "Open Sans", sans-serif;
    color: var(--ink);
  }
  .brand-band {
    position: absolute;
    left: 53px; top: 90px;
    width: 829px; height: 112px;
    background: var(--brand-red);
    display: flex;
    align-items: center;
    gap: 16px;
    padding-left: 10px;
    box-sizing: border-box;
  }
  .brand-mark {
    width: 52px; height: 52px;
    border-radius: 50%;
    background: var(--logo-dot);
    flex: none;
  }
  .brand-name {
    font-weight: 400;
    font-size: 42px;
    color: var(--logo-text);
    letter-spacing: 0.5px;
  }
  .sender-block {
    position: absolute;
    left: 54px; top: 218px;
    font-size: 13px;
    line-height: 16px;
  }
  .sender-block .firm {
    font-weight: 700;
    letter-spacing: 0.6px;
  }
  .sender-block .date {
    margin-top: 22px;
  }
  .doc-title {
    position: absolute;
    right: 47px; top: 208px;
    margin: 0;
    font-size: 110px;
    font-weight: 400;
    line-height: 1;
    letter-spacing: 1px;
  }
  .routing {
    position: absolute;
    left: 45px; top: 365px;
    width: 844px;
  }
  .routing-row {
    display: flex;
    height: 28.7px;
    border-top: 1px solid var(--rule);
    box-sizing: border-box;
    font-size: 14px;
  }
  .routing-row:last-child { border-bottom: 1px solid var(--rule); height: 29.7px; }
  .routing-cell {
    box-sizing: border-box;
    padding: 10px 0 0 10px;
    line-height: 1;
    white-space: nowrap;
  }
  .routing-cell.left { width: 370px; border-right: 1px solid var(--rule); }
  .routing-cell.right { flex: 1; padding-left: 8px; }
  .routing-cell .big { font-size: 18px; position: relative; top: -1px; }
  .label-strong { font-weight: 700; }
  .memo {
    position: absolute;
    left: 45px; top: 508px;
    width: 844px;
  }
  .memo-row {
    height: 28.7px;
    border-bottom: 1px solid var(--rule);
    box-sizing: border-box;
    padding: 10px 0 0 10px;
    font-size: 14px;
    line-height: 1;
  }
  .comments {
    position: absolute;
    left: 55px; top: 590px;
    font-size: 14px;
    line-height: 20px;
  }
  .comments h2 {
    margin: 0;
    font-size: 15px;
    font-weight: 700;
    letter-spacing: 0.3px;
  }
  .handling {
    position: absolute;
    left: 41px; top: 980px;
    width: 844px;
    border-top: 1px solid var(--rule);
    padding: 9px 0 0 0;
    margin: 0;
    list-style: none;
  }
  .handling li {
    display: flex;
    align-items: center;
    gap: 11px;
    height: 37px;
    font-size: 15px;
  }
  .checkbox {
    width: 20px; height: 19px;
    border: 1px solid #666;
    box-sizing: border-box;
    margin-left: 2px;
    flex: none;
  }
  .footer-band {
    position: absolute;
    left: 41px; top: 1145px;
    width: 844px; height: 11px;
    background: var(--brand-red);
  }
</style>
</head>
<body>
<div class="sheet">
  <header class="brand-band">
    <span class="brand-mark"></span>
    <span class="brand-name">Vireo Associates</span>
  </header>

  <div class="sender-block">
    <div class="firm">VIREO ASSOCIATES, LLC</div>
    <div>www.vireoassociates-example.com</div>
    <div>P 703 614 2290</div>
    <div>F 703 286 7135</div>
    <div class="date">[Pick the date]</div>
  </div>

  <h1 class="doc-title">Fax</h1>

  <div class="routing">
    <div class="routing-row">
      <div class="routing-cell left"><span class="label-strong">TO:</span> <span class="big">«GreetingLine»</span></div>
      <div class="routing-cell right"><span class="label-strong">FROM: Helen</span></div>
    </div>
    <div class="routing-row">
      <div class="routing-cell left">[TYPE THE RECIPIENT COMPANY NAME]</div>
      <div class="routing-cell right">PAGES:&nbsp; [Type the number of pages]</div>
    </div>
    <div class="routing-row">
      <div class="routing-cell left">FAX: «Business Fax»</div>
      <div class="routing-cell right">FAX:&nbsp; [Type the sender fax number]</div>
    </div>
    <div class="routing-row">
      <div class="routing-cell left">PHONE: «Business Phone»</div>
      <div class="routing-cell right">PHONE:&nbsp; [Type the sender phone number]</div>
    </div>
    <div class="routing-row">
      <div class="routing-cell left"></div>
      <div class="routing-cell right"></div>
    </div>
  </div>

  <div class="memo">
    <div class="memo-row">CC: [Type text]</div>
    <div class="memo-row">RE: [Type text]</div>
  </div>

  <section class="comments">
    <h2>COMMENTS:</h2>
    <div>[Type comments]</div>
  </section>

  <ul class="handling">
    <li><span class="checkbox"></span>Urgent</li>
    <li><span class="checkbox"></span>Please review</li>
    <li><span class="checkbox"></span>Please comment</li>
    <li><span class="checkbox"></span>For your records</li>
  </ul>

  <div class="footer-band"></div>
</div>
</body>
</html>
```